Business cards / Letterheads / Compliment slips

We are looking to get business cards, letterheads and compliment slips designed.

These will all have to follow the design of our new website and logo. Links to the website, logo and fonts can be found below...

The designs need to be simple with focus on the typography. Only the following colours should be used on the designs...

#7f9d3c
#191818
#fff

Website:
http://brightfieldweb.samplework.co.uk/

Logo:
https://www.filecrate.example/sh/9xk2mwq7tvbalp4/qrtuPL8NzK/logos

Fonts:
https://www.filecrate.example/sh/9xk2mwq7tvbalp4/Hw7ZpRt3sQ/Fonts/BayerModern_TTF

and

https://www.filecrate.example/sh/9xk2mwq7tvbalp4/T6nVyo4Dc1/Fonts/MuseoSansFamily

Reason: We would like some more design submissions

Reason: We are still deciding on designs we like and would like to see some more submissions...

Industry/Entity Type

Business

Requirements
Must have
• The designs need to be simple with focus on the typography. Only the following colours should be used on the designs...

#7f9d3c
#191818
#fff
Should not have
• - Any fonts that are not provided.
- Any colours that are not provided.

```html
<!DOCTYPE html>
<html lang="en">
<head>
<meta charset="utf-8">
<title>brightfieldweb – Business Cards</title>
<link rel="stylesheet" href="https://fonts.googleapis.com/css2?family=Nunito+Sans:wght@400;700;800&display=swap">
<style>
  :root {
    --green: #7f9d3c;
    --charcoal: #2f3030;
    --ink: #191818;
    --paper: #ffffff;
    --backdrop: #e6e4e0;
    --soft-text: #d9d9d9;
  }
  * { box-sizing: border-box; margin: 0; padding: 0; }
  html, body {
    width: 1200px;
    height: 880px;
    overflow: hidden;
  }
  body {
    background: var(--backdrop);
    font-family: "Nunito Sans", Arial, sans-serif;
    display: flex;
    align-items: center;
    justify-content: center;
    gap: 40px;
  }
  .card {
    width: 540px;
    height: 310px;
    position: relative;
    box-shadow: 0 6px 18px rgba(0,0,0,0.18);
  }

  /* Dark front card */
  .card--front {
    background: var(--charcoal);
    color: var(--paper);
  }
  .card--front .brand {
    position: absolute;
    left: 0; right: 0;
    top: 118px;
    display: flex;
    align-items: center;
    justify-content: center;
    gap: 14px;
  }
  .card--front .web-address {
    position: absolute;
    left: 0; right: 0;
    bottom: 30px;
    text-align: center;
    font-size: 15px;
    letter-spacing: 1.5px;
    color: var(--soft-text);
  }

  /* Brand lockup */
  .brand-dot {
    width: 46px;
    height: 46px;
    border-radius: 50%;
    background: var(--green);
    flex: none;
  }
  .brand-name {
    font-weight: 800;
    font-size: 46px;
    letter-spacing: -0.5px;
    color: var(--green);
    line-height: 1;
  }

  /* White back card */
  .card--back {
    background: var(--paper);
    color: var(--ink);
  }
  .card--back .brand {
    position: absolute;
    right: 34px;
    top: 48px;
    display: flex;
    align-items: center;
    gap: 12px;
  }
  .card--back .brand-dot { width: 40px; height: 40px; }
  .card--back .brand-name { font-size: 40px; }

  .holder {
    position: absolute;
    left: 44px;
    top: 168px;
    width: 190px;
    text-align: right;
  }
  .holder-name {
    font-weight: 700;
    font-size: 18px;
    color: var(--green);
  }
  .holder-role {
    font-size: 12px;
    color: var(--ink);
    margin-top: 2px;
  }
  .divider {
    position: absolute;
    left: 250px;
    top: 176px;
    width: 1px;
    height: 82px;
    background: var(--ink);
  }
  .contact {
    position: absolute;
    left: 266px;
    top: 190px;
    list-style: none;
    font-size: 13px;
    line-height: 19px;
    color: var(--ink);
  }
</style>
</head>
<body>
  <section class="card card--front" aria-label="Business card front">
    <div class="brand">
      <span class="brand-dot"></span>
      <span class="brand-name">brightfieldweb</span>
    </div>
    <p class="web-address">www.brightfieldweb.co.uk</p>
  </section>

  <section class="card card--back" aria-label="Business card back">
    <div class="brand">
      <span class="brand-dot"></span>
      <span class="brand-name">brightfieldweb</span>
    </div>
    <div class="holder">
      <p class="holder-name">Name Surname</p>
      <p class="holder-role">manager</p>
    </div>
    <span class="divider"></span>
    <ul class="contact">
      <li>P. +00 123 456 789</li>
      <li>F. +00 123 456 789</li>
      <li>office@brightfieldweb.co.uk</li>
    </ul>
  </section>
</body>
</html>
```